Business Card Design For Marketing Agnecy LVT

Need business card design for marketing agency.

Dorian Pell
President, CEO
1-555-304-2917
dorian@lumenvaletrewards.net
www.LumenValeTrewards.biz

Back Side:
Boost Sales Using Rewards, Incentives & Giveaways
Get A Free Sample Package

Target Market(s)

B2B

Industry/Entity Type

Marketing

Contact Information for Business Card

Dorian Pell
President, CEO
1-555-304-2917

Back Side:
Get A Free Sample Package

Please note that my current url is OLD DESIGN. I am working on new design and want the business card to match color themes at least on new site. Here is the demo link for new site so you can see the colors I use, etc.

http://pagekilnstudio.example/qx/dorian/lvt_final/index.html

Requirements
Must have
• Please note that my current url is OLD DESIGN. I am working on new design and want the business card to match color themes at least on new site. Here is the demo link for new site so you can see the colors I use, etc.

Nice to have

Should not have

```html
<!DOCTYPE html>
<html lang="en">
<head>
<meta charset="utf-8">
<title>LVT Business Card</title>
<link rel="stylesheet" href="https://fonts.googleapis.com/css2?family=Montserrat:wght@400;600;700&family=Open+Sans:wght@600;700&display=swap">
<style>
:root{
  --bg:#3a3b3d;
  --bg-dark:#222325;
  --brand-blue:#1f74c0;
  --ink-grey:#4d4f53;
  --slab-grey:#5f6165;
  --paper:#ffffff;
  --ink-dark:#2b2b2b;
}
*{margin:0;padding:0;box-sizing:border-box}
html,body{width:1200px;height:1000px;overflow:hidden}
body{background:radial-gradient(ellipse at 55% 40%,var(--bg),var(--bg-dark));position:relative;font-family:"Montserrat",sans-serif}
.card{position:absolute;width:600px;height:343px;border-radius:22px;overflow:hidden;box-shadow:0 14px 30px rgba(0,0,0,.45)}
.card-back{left:80px;top:90px;background:var(--brand-blue)}
.card-front{left:520px;top:560px;background:var(--paper)}

/* back */
.back-mark{position:absolute;left:170px;top:40px;font-family:"Open Sans",sans-serif;font-weight:700;font-size:170px;color:rgba(255,255,255,.13);letter-spacing:-4px}
.back-lines{position:absolute;left:0;right:0;top:62px;text-align:center;color:var(--paper);font-family:"Open Sans",sans-serif;font-weight:600;font-size:29px;line-height:52px}
.back-band{position:absolute;left:0;right:0;top:258px;height:56px;background:var(--paper);display:flex;align-items:center;justify-content:center;font-family:"Open Sans",sans-serif;font-weight:700;font-size:18px;color:var(--ink-dark)}

/* front */
.brand{position:absolute;left:36px;top:112px;width:200px;display:flex;align-items:center;gap:10px}
.brand-dot{width:16px;height:16px;border-radius:50%;background:var(--brand-blue)}
.brand-name{font-weight:700;font-size:64px;color:var(--brand-blue);letter-spacing:1px}
.divider{position:absolute;left:256px;top:48px;width:2px;height:220px;background:var(--ink-grey)}
.person{position:absolute;left:276px;top:46px}
.person-name{font-weight:700;font-size:28px;color:var(--brand-blue)}
.person-role{font-weight:400;font-size:22px;color:var(--ink-grey);margin-top:4px}
.contacts{position:absolute;left:276px;top:140px;right:24px;list-style:none}
.contact{display:flex;align-items:center;gap:10px;height:40px;font-size:14px;font-weight:600;color:var(--ink-dark);white-space:nowrap}
.contact svg{width:26px;height:26px;flex:none}
.trim{position:absolute;left:0;bottom:0}
</style>
</head>
<body>

<section class="card card-back">
  <div class="back-mark" aria-hidden="true">LVT</div>
  <div class="back-lines">
    <p>Boost Sales Using Rewards</p>
    <p>Incentives &amp; Giveaways</p>
    <p>Get A Free Sample Package</p>
  </div>
  <div class="back-band">www.lumenvaletrewards.biz</div>
</section>

<section class="card card-front">
  <div class="brand">
    <span class="brand-dot"></span>
    <span class="brand-name">LVT</span>
  </div>
  <div class="divider"></div>
  <div class="person">
    <p class="person-name">DORIAN PELL</p>
    <p class="person-role">CEO</p>
  </div>
  <ul class="contacts">
    <li class="contact">
      <svg viewBox="0 0 26 26"><rect width="26" height="26" rx="5" fill="#1f74c0"/><rect x="8.5" y="5" width="9" height="16" rx="1.5" fill="none" stroke="#fff" stroke-width="2"/><circle cx="13" cy="18" r="1" fill="#fff"/></svg>
      1-555-304-2917
    </li>
    <li class="contact">
      <svg viewBox="0 0 26 26"><rect width="26" height="26" rx="5" fill="#1f74c0"/><rect x="5" y="8" width="16" height="11" fill="none" stroke="#fff" stroke-width="2"/><path d="M5 8l8 6 8-6" fill="none" stroke="#fff" stroke-width="2"/></svg>
      dorian@lumenvaletrewards.net
    </li>
    <li class="contact">
      <svg viewBox="0 0 26 26"><rect width="26" height="26" rx="5" fill="#1f74c0"/><circle cx="13" cy="13" r="7" fill="none" stroke="#fff" stroke-width="2"/><path d="M6 13h14M13 6c-3 4-3 10 0 14M13 6c3 4 3 10 0 14" fill="none" stroke="#fff" stroke-width="1.5"/></svg>
      www.LumenValeTrewards.biz
    </li>
  </ul>
  <svg class="trim" width="600" height="70" viewBox="0 0 600 70">
    <polygon points="0,70 0,62 470,28 450,70" fill="#1f74c0"/>
    <polygon points="470,28 600,20 600,70 450,70" fill="#5f6165"/>
  </svg>
</section>

</body>
</html>
```